Real Estate Seller Financing Postcard

I need a postcard that lays out these options contained in the notes that grabs attention, explains the two options easily and is eye-catching. The front needs to have the percentages on it and information about it and on the other side One side exact Text is:
"Monthly income without tenant headaches" in big letters. Also on front "Get
110%
add an "or"
160% of market value for your property. ". The percentages should be displayed and that is not to be a sentence of text. Other side text: I need bullets points for these "Formal protection as a lien holder against home
No commission or closing cost
Fast closings possible
Property taken as is so no repairs.

Add to the top of the back in "It’s simple. I am a new investor without down payment capital who still want to double our portfolio this year to grow our portfolio."
Here are the two options that are to be the largest part of the back
Option 1, you can receive 80% now cash and 30% over a short period of time including interest.

Option 2, where act like a bank allowing you to make 150% if you finance the whole property(ies). No gimmicks and surprises, just simple unconventional financing.

Include Logo Somewhere

Target Market(s)

Property Owners Wanting to Sell Their Property

Industry/Entity Type

Real Estate Investing

Requirements
Must have
• The options promiment and each side with its respective information. Must have logo somewhere
Nice to have
• The options in color other than black.
Should not have
• A picture of money on the front. Any other image is okay.

```html
<!DOCTYPE html>
<html lang="en">
<head>
<meta charset="utf-8">
<title>Seller Financing Postcard</title>
<link rel="stylesheet" href="https://fonts.googleapis.com/css2?family=Montserrat:wght@400;500;600;700&family=Oswald:wght@200;300;500;600&family=Poppins:ital,wght@0,300;1,300;1,800;1,900&display=swap">
<style>
  :root {
    --page: #dedede;
    --navy: #0b2460;
    --navy-deep: #061a4a;
    --royal: #0f3a94;
    --brand: #1f4aa8;
    --sky: #0a66b0;
    --silver-hi: #f4f4f4;
    --silver-lo: #b9bcc2;
    --ink: #1b1b1b;
    --grey-type: #8a8a8a;
    --white: #ffffff;
  }
  * { margin: 0; padding: 0; box-sizing: border-box; }
  html, body { width: 849px; height: 1200px; overflow: hidden; }
  body { background: var(--page); position: relative; font-family: "Montserrat", sans-serif; }

  .card { position: absolute; left: 45px; width: 758px; height: 515px; overflow: hidden; }
  .card--front { top: 76px; background: var(--white); }
  .card--back { top: 609px; background: linear-gradient(180deg, var(--navy-deep) 0%, var(--royal) 45%, var(--navy-deep) 100%); }
  .card-art { position: absolute; inset: 0; }

  /* front */
  .front-band { position: absolute; left: 0; top: 278px; width: 758px; height: 237px;
    background: radial-gradient(ellipse at 55% 30%, #1a4a9e 0%, var(--navy) 55%, var(--navy-deep) 100%); }
  .headline-get { position: absolute; left: 33px; top: 22px; font: italic 900 78px/1 "Poppins", sans-serif;
    color: var(--brand); letter-spacing: -2px; }
  .pill { position: absolute; border-radius: 26px;
    background: linear-gradient(180deg, var(--silver-hi), var(--silver-lo));
    box-shadow: 0 4px 8px rgba(0,0,0,.3); transform: skewX(-8deg); }
  .pill--main { left: 40px; top: 104px; width: 300px; height: 141px; }
  .pill--alt { left: 160px; top: 256px; width: 182px; height: 86px; border-radius: 20px; }
  .figure { position: absolute; font-family: "Poppins", sans-serif; font-style: italic; font-weight: 900;
    color: var(--brand); letter-spacing: -3px; line-height: 1; }
  .figure--main { left: 52px; top: 117px; font-size: 108px; }
  .figure--alt { left: 174px; top: 272px; font-size: 56px; letter-spacing: -1px; }
  .headline-or { position: absolute; left: 66px; top: 254px; font: 600 80px/1 "Oswald", sans-serif;
    color: var(--brand); transform: skewX(-8deg) scaleX(.86); transform-origin: left top; }
  .value-line { position: absolute; left: 20px; width: 320px; text-align: center; color: var(--white); font-family: "Oswald", sans-serif; line-height: 1; }
  .value-line--light { top: 384px; font-weight: 200; font-size: 38px; }
  .value-line--bold { top: 420px; font-weight: 600; font-size: 44px; }

  .brand { position: absolute; left: 472px; top: 31px; display: flex; align-items: center; gap: 14px; }
  .brand-mark { width: 76px; height: 76px; border-radius: 50%; border: 2px solid var(--brand); flex: none; }
  .brand-name { font: 700 16px/1.3 "Montserrat", sans-serif; color: var(--brand); white-space: nowrap; }

  .tagline { position: absolute; right: 29px; top: 120px; text-align: right; line-height: 1; }
  .tagline-thin { display: block; font: 200 55px/1 "Oswald", sans-serif; color: var(--ink); }
  .tagline-grey { display: block; font: 600 52px/1 "Oswald", sans-serif; color: var(--grey-type); margin-top: -4px; }
  .tagline-blue { display: block; font: 700 47px/1 "Montserrat", sans-serif; color: var(--brand); }
  .tagline-rule { position: absolute; left: 393px; top: 265px; width: 335px; height: 2px; background: #555; }

  .benefits { position: absolute; left: 405px; top: 327px; list-style: none; color: var(--white); font-size: 15px; line-height: 1.15; }
  .benefits li { position: relative; padding-left: 29px; margin-bottom: 17px; max-width: 320px; }
  .benefits li svg { position: absolute; left: 0; top: -6px; }

  /* back */
  .intro-band { position: absolute; left: 0; top: 30px; width: 758px; height: 98px; background: var(--sky); }
  .intro { position: absolute; left: 31px; top: 37px; width: 360px; color: var(--white); font: 600 15.5px/20px "Montserrat", sans-serif; white-space: nowrap; }
  .intro-lead { font-weight: 400; font-size: 21px; }
  .steps-tab { position: absolute; left: 48px; top: 144px; width: 207px; height: 40px; border-radius: 14px;
    background: linear-gradient(180deg, var(--silver-hi), var(--silver-lo)); transform: skewX(-8deg);
    box-shadow: 0 3px 6px rgba(0,0,0,.35); }
  .steps-title { position: absolute; left: 56px; top: 143px; font: italic 800 28px/40px "Poppins", sans-serif; color: var(--navy); }
  .steps-box { position: absolute; left: 23px; top: 167px; width: 333px; height: 212px; border: 1.5px solid var(--white); border-radius: 22px; }
  .options { position: absolute; left: 15px; top: 192px; width: 332px; list-style: none; }
  .option { position: relative; padding-left: 35px; margin-bottom: 8px; color: var(--white);
    font: italic 300 14.5px/18px "Poppins", sans-serif; }
  .option svg { position: absolute; left: 0; top: 0; }
  .option-label { font-weight: 800; }
  .option em { font-style: italic; font-size: 19px; font-weight: 300; color: #d6dbe6; }
  .illustration { position: absolute; top: 398px; width: 90px; height: 90px; border-radius: 50%;
    background: radial-gradient(circle at 40% 35%, #ffffff 0%, #c8cbd1 55%, #8e939c 100%);
    box-shadow: 0 4px 10px rgba(0,0,0,.4); }
  .illustration--growth { left: 40px; }
  .illustration--balance { left: 158px; }
  .illustration--home { left: 277px; }

  .stamp-box { position: absolute; left: 640px; top: 31px; width: 88px; height: 88px; border: 2px solid #000; }
  .address-line { position: absolute; left: 429px; width: 329px; height: 1.5px; background: #000; }
</style>
</head>
<body>

<section class="card card--front" aria-label="Postcard front">
  <div class="front-band"></div>
  <svg class="card-art" width="758" height="515" viewBox="0 0 758 515" aria-hidden="true">
    <defs>
      <linearGradient id="bubble" x1="0" y1="0" x2="1" y2="1">
        <stop offset="0" stop-color="#f2f2f2"/>
        <stop offset="1" stop-color="#dcdcdc"/>
      </linearGradient>
    </defs>
    <ellipse cx="170" cy="160" rx="248" ry="214" fill="#2f5fc4"/>
    <ellipse cx="165" cy="154" rx="245" ry="206" fill="url(#bubble)"/>
  </svg>

  <div class="headline-get">GET</div>
  <div class="pill pill--main"></div>
  <div class="figure figure--main">110%</div>
  <div class="headline-or">OR</div>
  <div class="pill pill--alt"></div>
  <div class="figure figure--alt">160%</div>
  <p class="value-line value-line--light">OF MARKET VALUE FOR</p>
  <p class="value-line value-line--bold">YOUR PROPERTY.</p>

  <div class="brand">
    <span class="brand-mark"></span>
    <span class="brand-name">HELIOS<br>REAL ESTATE GROUP</span>
  </div>

  <h1 class="tagline">
    <span class="tagline-thin">MONTHLY INCOME</span>
    <span class="tagline-grey">WITHOUT TENANT</span>
    <span class="tagline-blue">HEADACHES</span>
  </h1>
  <div class="tagline-rule"></div>

  <ul class="benefits">
    <li><svg width="26" height="26" viewBox="0 0 26 26"><path d="M2 14 L9 24 L25 2 L10 17 Z" fill="#3d6fd6" stroke="#cfe0ff" stroke-width="1"/></svg>Formal protection as a lien holder against home</li>
    <li><svg width="26" height="26" viewBox="0 0 26 26"><path d="M2 14 L9 24 L25 2 L10 17 Z" fill="#3d6fd6" stroke="#cfe0ff" stroke-width="1"/></svg>No commission or closing cost</li>
    <li><svg width="26" height="26" viewBox="0 0 26 26"><path d="M2 14 L9 24 L25 2 L10 17 Z" fill="#3d6fd6" stroke="#cfe0ff" stroke-width="1"/></svg>Fast closings possible</li>
    <li><svg width="26" height="26" viewBox="0 0 26 26"><path d="M2 14 L9 24 L25 2 L10 17 Z" fill="#3d6fd6" stroke="#cfe0ff" stroke-width="1"/></svg>Property taken as is so no repairs.</li>
  </ul>
</section>

<section class="card card--back" aria-label="Postcard back">
  <div class="intro-band"></div>
  <svg class="card-art" width="758" height="515" viewBox="0 0 758 515" aria-hidden="true">
    <path d="M500 0 Q360 120 368 259 Q372 400 478 515 L758 515 L758 0 Z" fill="#3a6fe0"/>
    <path d="M510 0 Q370 120 376 259 Q380 400 488 515 L758 515 L758 0 Z" fill="#9a9a9a"/>
    <path d="M522 0 Q380 120 386 259 Q390 400 500 515 L758 515 L758 0 Z" fill="#ffffff"/>
  </svg>

  <p class="intro"><span class="intro-lead">It’s simple.</span> I am a new investor without<br>down payment capital who still want<br>to double our portfolio this year to<br>grow our portfolio.</p>

  <div class="steps-box"></div>
  <div class="steps-tab"></div>
  <h2 class="steps-title">How it works</h2>
  <ul class="options">
    <li class="option">
      <svg width="28" height="28" viewBox="0 0 28 28" aria-hidden="true"><circle cx="14" cy="14" r="12.5" fill="#1f4aa8" stroke="#d9dde6" stroke-width="2.5"/><path d="M9 14.5 L12.5 18 L19 10.5" fill="none" stroke="#fff" stroke-width="2"/></svg>
      <span class="option-label">Option 1,</span> you can receive <em>80%</em> now cash and <em>30%</em> over a short period of time including interest.
    </li>
    <li class="option">
      <svg width="28" height="28" viewBox="0 0 28 28" aria-hidden="true"><circle cx="14" cy="14" r="12.5" fill="#1f4aa8" stroke="#d9dde6" stroke-width="2.5"/><path d="M9 14.5 L12.5 18 L19 10.5" fill="none" stroke="#fff" stroke-width="2"/></svg>
      <span class="option-label">Option 2,</span> where act like a bank allowing you to make <em>150%</em> if you finance the whole property(ies). No gimmicks and surprises, just simple unconventional financing.
    </li>
  </ul>

  <div class="illustration illustration--growth" role="img" aria-label="Illustration of a building with a rising arrow"></div>
  <div class="illustration illustration--balance" role="img" aria-label="Illustration of a house balanced against coins"></div>
  <div class="illustration illustration--home" role="img" aria-label="Illustration of a house with coins"></div>

  <div class="stamp-box"></div>
  <div class="address-line" style="top:310px"></div>
  <div class="address-line" style="top:350px"></div>
  <div class="address-line" style="top:388px"></div>
  <div class="address-line" style="top:426px"></div>
</section>

</body>
</html>
```